A start-up named "Corvath Therapeutics" - needs a new PowerPoint design

We need a new PowerPoint Design for an early-stage start-up named "Corvath Therapeutics" seeking to disrupt the current approach towards drug discovery within aging disorders.

We would like to build on Corvath's legacy, the founder of the modern science of genetics, by employing a multidisciplinary approach, experimenting, and providing elderly patients the attention they deserve.

We have selected the suffix "therapeutics" intentionally as it stands for (a medicine) the treatment of disease; the science of healing. Alzheimer’s treatment is a huge, urgent, unmet need:
- Shift from a disease-management system to a preventive medicine system
- Focus on increasing the health span, not only the life span

Target Market(s)

Pharma/ Biotech Executives Medical Institutions Healthcare professionals (MDs, nurses, payors, pharmacists, etc.) Patients

Industry/Entity Type

Healthcare

Other font styles liked:
• Celias

Colors
0054AA
0677BA
7BADD7
CADEEF
E8F1F8
E54698
E96AAD
F1A4CE
F9D9EA
FCEFF6
A7469A
B969AE
D3A5CF
EDDBEB
F8F0F9
6B429C
8869AF
B7A5CE
E3DAEB
F3F0F8

Requirements
Must have
• - differentiate from other companies named after Corvath - differentiate from other Pharma/ Biotech companies
Nice to have
• simplicity/ minimalist logo vivid colors gradient 3D Life-Sciences inspired Simple geometry Balance
Should not have
• mascot/ emblem watermark logo animated ink style nature-inspired inventive typography artistic chaos

```html
<!DOCTYPE html>
<html lang="en">
<head>
<meta charset="utf-8">
<title>Corvath Therapeutics – Presentation Slides</title>
<link href="https://fonts.googleapis.com/css2?family=Roboto:ital,wght@0,300;0,400;0,500;0,700;1,400&family=Roboto+Condensed:wght@300;400;700&display=swap" rel="stylesheet">
<style>
:root{
  --stage:#2a2a2c;
  --blue-deep:#0054aa;
  --blue:#0677ba;
  --blue-sky:#1fa3e6;
  --blue-light:#7badd7;
  --magenta:#c41e8f;
  --pink:#e54698;
  --orchid:#a7469a;
  --purple:#6b429c;
  --navy:#233a8f;
  --ink:#222;
  --grey-text:#666;
  --grey-soft:#e6e6e8;
  --white:#fff;
}
*{box-sizing:border-box;margin:0;padding:0}
html,body{width:1200px;height:546px;overflow:hidden;background:var(--stage)}
body{position:relative;font-family:"Roboto",Arial,sans-serif;color:var(--ink)}
.slide{position:absolute;width:337px;height:190px;overflow:hidden;background:var(--white)}
.slide--cover{left:73px;top:59px;background:linear-gradient(110deg,#5a2ca0 0%,#b01d8f 55%,#7a2ea8 100%)}
.slide--text{left:432px;top:59px}
.slide--team{left:792px;top:59px;background:#ececee}
.slide--chart{left:73px;top:275px}
.slide--stats{left:432px;top:275px}
.slide--contact{left:792px;top:275px;background:linear-gradient(120deg,#1a8fd6 0%,#14a6ea 50%,#0677ba 100%)}
.layer{position:absolute;inset:0}
.photo{position:absolute}
.brand{position:absolute;display:flex;align-items:center;gap:5px;font-family:"Roboto",Arial,sans-serif;font-weight:500;line-height:1}
.brand__mark{width:8px;height:8px;background:currentColor;flex:none}
.brand__name{display:flex;flex-direction:column}
.brand__sub{font-size:.42em;letter-spacing:.12em;margin-top:2px}
.title{position:absolute;font-family:"Roboto",Arial,sans-serif;font-weight:700;white-space:nowrap;display:flex;align-items:center;gap:5px}
.badge{font-weight:400;font-style:italic;color:var(--white);padding:1px 3px;border-radius:2px}
.slide-no{position:absolute;font-family:"Roboto Condensed",Arial,sans-serif;font-weight:400;line-height:1;background:linear-gradient(90deg,var(--blue) 0%,var(--magenta) 100%);-webkit-background-clip:text;background-clip:text;color:transparent}
.fine{font-size:2.6px;line-height:1.45;color:var(--grey-text);text-align:justify}
/* cover */
.cover__tag{position:absolute;left:164px;top:139px;color:var(--white);font-family:"Roboto Condensed",Arial,sans-serif;font-size:15.5px;font-weight:300;border-bottom:.6px solid var(--white);padding-bottom:1px}
.cover__tag b{font-weight:700}
.cover__web{position:absolute;left:195px;top:160px;color:var(--white);font-size:5px;letter-spacing:.28em}
/* text slide */
.text__rule{position:absolute;left:16px;right:16px;top:41px;height:.7px;background:var(--magenta)}
.text__col{position:absolute;top:45px;width:144px}
.text__lead{font-size:5.3px;margin-bottom:3px;color:var(--ink)}
.text__col .fine{margin-bottom:6px}
.text__footer{position:absolute;left:50px;top:168px;display:flex;align-items:flex-end;gap:4px;width:228px}
.text__footer span{font-family:"Roboto Condensed",Arial,sans-serif;font-size:12px;font-weight:300}
.text__footer b{font-size:15px;font-weight:700;font-family:"Roboto Condensed",Arial,sans-serif}
.text__footer i{flex:1;height:.6px;background:var(--magenta);margin-bottom:3px}
/* team */
.member{position:absolute;display:flex;gap:8px}
.member__icon{width:42px;height:42px;flex:none}
.member__name{font-size:6.4px;margin-top:-1px;color:var(--ink)}
.member__bio{font-size:4px;line-height:1.55;color:#888;width:44px;margin-top:3px}
.member__phone{font-size:3.8px;color:#888;margin-top:3px}
.member__links{display:flex;gap:4px;margin-top:3px}
.member__links i{width:3px;height:3px;border-radius:50%;background:#999}
/* chart */
.chart{position:absolute;left:16px;top:28px}
.chart__note{position:absolute;top:170px;width:28px;font-size:2.2px;line-height:1.4;color:#999;text-align:justify}
/* stats */
.stat{position:absolute;top:42px;width:52px;text-align:center}
.stat__label{font-size:3.7px;color:var(--ink);margin:3px 0 4px}
.stat .fine{font-size:2.2px;text-align:center;margin-bottom:2px}
/* contact */
.contact__line{position:absolute;left:17px;color:var(--white);font-family:"Roboto",Arial,sans-serif}
</style>
</head>
<body>

<!-- Slide 1: cover -->
<section class="slide slide--cover">
  <div class="photo" role="img" aria-label="Photo of a scientist working in a laboratory, tinted magenta" style="left:170px;top:0;width:167px;height:190px;background:radial-gradient(ellipse at 40% 45%,rgba(240,120,190,.45),rgba(176,29,143,0) 70%)"></div>
  <svg class="layer" viewBox="0 0 337 190" aria-hidden="true">
    <defs>
      <linearGradient id="coverBand" x1="0" y1="0" x2="1" y2="1">
        <stop offset="0" stop-color="#2a5fd0"/><stop offset=".5" stop-color="#1aa6ea"/><stop offset="1" stop-color="#1370c9"/>
      </linearGradient>
    </defs>
    <polygon points="0,0 60,0 0,80" fill="#1f3fae" opacity=".85"/>
    <polygon points="8,0 22,0 160,190 146,190" fill="url(#coverBand)"/>
    <polygon points="0,95 12,95 0,112" fill="url(#coverBand)"/>
    <polygon points="38,0 48,0 190,190 180,190" fill="#4a6fe0" opacity=".55"/>
    <polygon points="0,150 26,190 10,190 0,175" fill="url(#coverBand)"/>
    <polygon points="70,0 80,0 0,110 0,96" fill="url(#coverBand)" opacity=".8"/>
  </svg>
  <div class="brand" style="left:186px;top:78px;font-size:22px;color:var(--white)">
    <span class="brand__mark"></span>
    <span class="brand__name">Corvath<span class="brand__sub" style="font-size:9.5px;letter-spacing:.1em">Therapeutics</span></span>
  </div>
  <div class="cover__tag">BUSINESS <b>PRESENTATION</b></div>
  <div class="cover__web">WWW.COMPANYNAME.COM</div>
</section>

<!-- Slide 2: text -->
<section class="slide slide--text">
  <div class="photo" role="img" aria-label="Faint grey illustration of branching neurons" style="inset:0;background:radial-gradient(ellipse at 85% 20%,#eeeeee,rgba(255,255,255,0) 55%),radial-gradient(ellipse at 70% 90%,#efefef,rgba(255,255,255,0) 50%)"></div>
  <div class="title" style="left:61px;top:18px;font-size:17px;color:var(--magenta)">LOREM IPSUM <span class="badge" style="font-size:10px;background:var(--magenta)">DOLOR SIT AMET</span></div>
  <div class="text__rule"></div>
  <div class="text__col" style="left:21px">
    <p class="text__lead">Lorem ipsum dolor sit amet, consectetur adipiscing elit.</p>
    <p class="fine">Early detection shapes every plan we build for ageing patients and their care teams.</p>
    <p class="fine">We combine genetics, data and clinical insight to find targets that slow decline. Each study is designed with clinicians and patients from the start, so results reach the clinic faster.</p>
    <p class="fine">Prevention first, health span over life span, and care that respects every patient.</p>
  </div>
  <div class="text__col" style="left:173px">
    <p class="text__lead">Lorem ipsum dolor sit amet, consectetur adipiscing elit.</p>
    <p class="fine">Early detection shapes every plan we build for ageing patients and their care teams.</p>
    <p class="fine">We combine genetics, data and clinical insight to find targets that slow decline. Each study is designed with clinicians and patients from the start, so results reach the clinic faster.</p>
    <p class="fine">Prevention first, health span over life span, and care that respects every patient.</p>
  </div>
  <div class="slide-no" style="left:8px;top:150px;font-size:38px">02</div>
  <div class="text__footer"><span>TITLE</span><b>SLIDE</b><i></i></div>
  <div class="brand" style="left:276px;top:168px;font-size:12px;color:var(--blue)">
    <span class="brand__name">Corvath<span class="brand__sub" style="font-size:5px">Therapeutics</span></span>
  </div>
</section>

<!-- Slide 3: team -->
<section class="slide slide--team">
  <div class="photo" role="img" aria-label="Faint grey pattern of virus particles" style="inset:0;background:radial-gradient(circle at 45% 40%,#f7f7f8,rgba(236,236,238,0) 45%),radial-gradient(circle at 80% 75%,#f6f6f7,rgba(236,236,238,0) 40%)"></div>
  <svg class="layer" viewBox="0 0 337 190" aria-hidden="true">
    <polygon points="0,0 40,0 0,50" fill="#d6d6d9"/>
    <polygon points="20,0 32,0 130,120 118,120" fill="#cfcfd3" opacity=".8"/>
    <polygon points="0,120 10,120 0,135" fill="#d4d4d7"/>
    <polygon points="60,150 72,150 40,190 28,190" fill="#d2d2d6"/>
    <polygon points="60,30 70,30 0,110 0,98" fill="#dcdce0"/>
  </svg>
  <div class="title" style="left:194px;top:7px;font-size:11px;color:var(--navy)">LOREM IPSUM <span class="badge" style="font-size:6px;background:var(--navy)">DOLOR SIT AMET</span></div>
  <div class="slide-no" style="left:27px;top:78px;font-size:40px">03</div>

  <div class="member" style="left:109px;top:38px">
    <svg class="member__icon" viewBox="0 0 42 42" aria-hidden="true"><polygon points="12,1 30,1 41,12 41,30 30,41 12,41 1,30 1,12" fill="var(--magenta)"/><polygon points="13,4 29,4 38,13 38,29 29,38 13,38 4,29 4,13" fill="var(--blue-sky)"/><circle cx="21" cy="21" r="9" fill="var(--white)"/></svg>
    <div><p class="member__name">Lena Marsh</p><p class="member__bio">Lorem ipsum dolor sit amet, consectetur adipiscing elit.</p><p class="member__phone">+123 456 789</p><p class="member__links"><i></i><i></i><i></i><i></i></p></div>
  </div>
  <div class="member" style="left:205px;top:77px">
    <svg class="member__icon" viewBox="0 0 42 42" aria-hidden="true"><polygon points="12,1 30,1 41,12 41,30 30,41 12,41 1,30 1,12" fill="var(--magenta)"/><polygon points="13,4 29,4 38,13 38,29 29,38 13,38 4,29 4,13" fill="var(--blue-sky)"/><circle cx="21" cy="21" r="9" fill="var(--white)"/></svg>
    <div><p class="member__name">Lena Marsh</p><p class="member__bio">Lorem ipsum dolor sit amet, consectetur adipiscing elit.</p><p class="member__phone">+123 456 789</p><p class="member__links"><i></i><i></i><i></i><i></i></p></div>
  </div>
  <div class="member" style="left:109px;top:119px">
    <svg class="member__icon" viewBox="0 0 42 42" aria-hidden="true"><polygon points="12,1 30,1 41,12 41,30 30,41 12,41 1,30 1,12" fill="var(--magenta)"/><polygon points="13,4 29,4 38,13 38,29 29,38 13,38 4,29 4,13" fill="var(--blue-sky)"/><circle cx="21" cy="21" r="9" fill="var(--white)"/></svg>
    <div><p class="member__name">Lena Marsh</p><p class="member__bio">Lorem ipsum dolor sit amet, consectetur adipiscing elit.</p><p class="member__phone">+123 456 789</p><p class="member__links"><i></i><i></i><i></i><i></i></p></div>
  </div>
  <div class="brand" style="left:288px;top:167px;font-size:12px;color:var(--blue)">
    <span class="brand__name">Corvath<span class="brand__sub" style="font-size:5px">Therapeutics</span></span>
  </div>
</section>

<!-- Slide 4: growth chart -->
<section class="slide slide--chart">
  <svg class="layer" viewBox="0 0 337 190" aria-hidden="true">
    <polygon points="236,0 337,0 337,60 250,0" fill="#efeff1"/>
    <polygon points="236,0 252,0 337,110 337,132" fill="#e4e4e7"/>
    <polygon points="236,0 246,0 246,190 236,190" fill="#f0f0f2"/>
    <polygon points="300,70 312,70 250,190 238,190" fill="#e9e9ec"/>
    <polygon points="280,150 337,120 337,134 290,160" fill="#eeeef0"/>
  </svg>
  <div class="title" style="left:18px;top:6px;font-size:15px;color:var(--magenta)">LOREM IPSUM <span style="font-weight:400;font-style:italic;font-size:8px;color:#555">DOLOR SIT AMET</span></div>
  <svg class="layer" viewBox="0 0 337 190" aria-hidden="true">
    <defs>
      <linearGradient id="barA" x1="0" y1="0" x2="0" y2="1"><stop offset="0" stop-color="#ffc23a"/><stop offset="1" stop-color="#ff9a1f"/></linearGradient>
      <linearGradient id="barB" x1="0" y1="0" x2="0" y2="1"><stop offset="0" stop-color="#f46aa3"/><stop offset="1" stop-color="#e5468f"/></linearGradient>
      <linearGradient id="barC" x1="0" y1="0" x2="0" y2="1"><stop offset="0" stop-color="#d45fb0"/><stop offset="1" stop-color="#a7469a"/></linearGradient>
      <linearGradient id="barD" x1="0" y1="0" x2="0" y2="1"><stop offset="0" stop-color="#8a56b8"/><stop offset="1" stop-color="#6b429c"/></linearGradient>
      <linearGradient id="barE" x1="0" y1="0" x2="0" y2="1"><stop offset="0" stop-color="#8f4bb0"/><stop offset="1" stop-color="#5b2f94"/></linearGradient>
    </defs>
    <g stroke="#e6e6e8" stroke-width=".4">
      <line x1="17" y1="30" x2="197" y2="30"/><line x1="17" y1="38" x2="197" y2="38"/><line x1="17" y1="46" x2="197" y2="46"/><line x1="17" y1="54" x2="197" y2="54"/><line x1="17" y1="62" x2="197" y2="62"/><line x1="17" y1="70" x2="197" y2="70"/><line x1="17" y1="78" x2="197" y2="78"/><line x1="17" y1="86" x2="197" y2="86"/><line x1="17" y1="94" x2="197" y2="94"/><line x1="17" y1="102" x2="197" y2="102"/><line x1="17" y1="110" x2="197" y2="110"/><line x1="17" y1="118" x2="197" y2="118"/><line x1="17" y1="126" x2="197" y2="126"/><line x1="17" y1="134" x2="197" y2="134"/><line x1="17" y1="142" x2="197" y2="142"/><line x1="17" y1="150" x2="197" y2="150"/>
    </g>
    <line x1="16" y1="157" x2="198" y2="157" stroke="#555" stroke-width=".8"/>
    <polygon points="27,157 27,141 40,131 53,141 53,157" fill="url(#barA)"/>
    <polygon points="60,157 60,120 73,110 86,120 86,157" fill="url(#barB)"/>
    <polygon points="93,157 93,109 106,99 119,109 119,157" fill="url(#barC)"/>
    <polygon points="126,157 126,92 139,82 152,92 152,157" fill="url(#barD)"/>
    <polygon points="160,157 160,72 173,62 186,72 186,157" fill="url(#barE)"/>
    <path d="M26,106 C32,100 36,97 40,96 C55,91 65,86 73,85 C88,82 96,78 106,75 C122,68 130,62 139,53 C150,42 160,34 173,29" fill="none" stroke="#aaa" stroke-width=".6"/>
    <circle cx="40" cy="96" r="2" fill="#ffae2a"/><circle cx="73" cy="85" r="2" fill="#ef5d9c"/><circle cx="106" cy="75" r="2" fill="#c653a8"/><circle cx="139" cy="53" r="2" fill="#7a4bad"/><circle cx="173" cy="29" r="2" fill="#6b3a9f"/>
    <g font-family="Roboto, Arial, sans-serif" font-size="9.5" font-weight="300" text-anchor="middle">
      <text x="40" y="127" fill="#ffa62a">+12.2</text>
      <text x="73" y="106" fill="#ef5d9c">+23.5</text>
      <text x="106" y="95" fill="#c653a8">+32.5</text>
      <text x="139" y="78" fill="#7a4bad">+43.3</text>
      <text x="173" y="57" fill="#6b3a9f">+55.5</text>
    </g>
    <rect x="26" y="163" width="28" height="5" fill="#ffb02a"/><rect x="59" y="163" width="28" height="5" fill="#ef5d9c"/><rect x="92" y="163" width="28" height="5" fill="#c653a8"/><rect x="125" y="163" width="28" height="5" fill="#7a4bad"/><rect x="159" y="163" width="28" height="5" fill="#6b3a9f"/>
    <g font-family="Roboto, Arial, sans-serif" font-size="3.4" fill="#fff" text-anchor="middle">
      <text x="40" y="166.8">January</text><text x="73" y="166.8">February</text><text x="106" y="166.8">March</text><text x="139" y="166.8">April</text><text x="173" y="166.8">June</text>
    </g>
  </svg>
  <p class="chart__note" style="left:26px">Short note on monthly growth.</p>
  <p class="chart__note" style="left:59px">Short note on monthly growth.</p>
  <p class="chart__note" style="left:92px">Short note on monthly growth.</p>
  <p class="chart__note" style="left:125px">Short note on monthly growth.</p>
  <p class="chart__note" style="left:159px">Short note on monthly growth.</p>
  <div class="slide-no" style="left:206px;top:158px;font-size:27px">04</div>
</section>

<!-- Slide 5: stats -->
<section class="slide slide--stats">
  <svg class="layer" viewBox="0 0 337 190" aria-hidden="true">
    <rect x="0" y="0" width="100" height="190" fill="#f6f6f7"/>
    <polygon points="0,0 30,0 100,90 100,112" fill="#e3e3e6"/>
    <polygon points="0,40 12,40 80,190 68,190" fill="#ebebee"/>
    <polygon points="60,0 74,0 0,92 0,76" fill="#dedee2"/>
    <polygon points="0,140 40,110 48,120 0,156" fill="#e6e6e9"/>
    <rect x="98" y="0" width="2" height="190" fill="#ececee"/>
  </svg>
  <div class="title" style="left:107px;top:13px;font-size:13px;color:var(--magenta)">LOREM IPSUM <span style="font-weight:400;font-style:italic;font-size:7.5px;color:var(--purple)">DOLOR SIT AMET</span></div>
  <div style="position:absolute;left:107px;right:4px;top:31px;height:.6px;background:var(--purple)"></div>

  <div class="stat" style="left:119px">
    <svg viewBox="0 0 40 40" width="40" height="40" aria-hidden="true"><circle cx="20" cy="20" r="16" fill="none" stroke="#eee" stroke-width="5"/><circle cx="20" cy="20" r="16" fill="none" stroke="#b0188a" stroke-width="5" stroke-dasharray="90.5 100.5" transform="rotate(-90 20 20)"/><text x="20" y="21.5" font-size="4.5" fill="#888" text-anchor="middle" font-family="Roboto, Arial, sans-serif">90%</text></svg>
    <p class="stat__label">Lorem ipsum dolor</p>
    <p class="fine">Focus on health span with early, preventive care for every patient.</p>
    <p class="fine">We combine genetics, data and clinical insight to find targets that slow decline. Each study is designed with clinicians and patients from the start, so results reach the clinic faster.</p>
  </div>
  <div class="stat" style="left:193px">
    <svg viewBox="0 0 40 40" width="40" height="40" aria-hidden="true"><circle cx="20" cy="20" r="16" fill="none" stroke="#eee" stroke-width="5"/><circle cx="20" cy="20" r="16" fill="none" stroke="#c653a8" stroke-width="5" stroke-dasharray="75.4 100.5" transform="rotate(-90 20 20)"/><text x="20" y="21.5" font-size="4.5" fill="#888" text-anchor="middle" font-family="Roboto, Arial, sans-serif">75%</text></svg>
    <p class="stat__label">Lorem ipsum dolor</p>
    <p class="fine">Focus on health span with early, preventive care for every patient.</p>
    <p class="fine">We combine genetics, data and clinical insight to find targets that slow decline. Each study is designed with clinicians and patients from the start, so results reach the clinic faster.</p>
  </div>
  <div class="stat" style="left:262px">
    <svg viewBox="0 0 40 40" width="40" height="40" aria-hidden="true"><circle cx="20" cy="20" r="16" fill="none" stroke="#eee" stroke-width="5"/><circle cx="20" cy="20" r="16" fill="none" stroke="#d47bbd" stroke-width="5" stroke-dasharray="60.3 100.5" transform="rotate(-90 20 20)"/><text x="20" y="21.5" font-size="4.5" fill="#888" text-anchor="middle" font-family="Roboto, Arial, sans-serif">60%</text></svg>
    <p class="stat__label">Lorem ipsum dolor</p>
    <p class="fine">Focus on health span with early, preventive care for every patient.</p>
    <p class="fine">We combine genetics, data and clinical insight to find targets that slow decline. Each study is designed with clinicians and patients from the start, so results reach the clinic faster.</p>
  </div>
  <div class="brand" style="left:107px;top:167px;font-size:11px;color:var(--blue)">
    <span class="brand__name">Corvath<span class="brand__sub" style="font-size:5px">Therapeutics</span></span>
  </div>
  <div class="slide-no" style="left:299px;top:158px;font-size:29px">05</div>
</section>

<!-- Slide 6: contact -->
<section class="slide slide--contact">
  <div class="photo" role="img" aria-label="Soft blue microscope image of cells" style="inset:0;background:radial-gradient(ellipse at 30% 60%,rgba(130,210,250,.35),rgba(20,166,234,0) 55%)"></div>
  <svg class="layer" viewBox="0 0 337 190" aria-hidden="true">
    <defs>
      <linearGradient id="contactBand" x1="0" y1="0" x2="1" y2="1"><stop offset="0" stop-color="#7a2ea8"/><stop offset="1" stop-color="#c41e8f"/></linearGradient>
    </defs>
    <polygon points="190,0 337,0 337,190 260,190 180,95" fill="url(#contactBand)" opacity=".9"/>
    <polygon points="200,0 214,0 337,130 337,146" fill="#1aa6ea" opacity=".85"/>
    <polygon points="250,0 262,0 180,110 168,110" fill="#2460c8" opacity=".8"/>
    <polygon points="310,0 324,0 324,190 310,190" fill="#1a8fd6" opacity=".7"/>
    <polygon points="200,190 214,190 280,110 266,110" fill="#8a3fb5"/>
  </svg>
  <div class="brand" style="left:18px;top:28px;font-size:25px;color:var(--white)">
    <span class="brand__mark" style="width:10px;height:10px"></span>
    <span class="brand__name">Corvath<span class="brand__sub" style="font-size:11px;letter-spacing:.1em">Therapeutics</span></span>
  </div>
  <p class="contact__line" style="top:146px;font-size:11px;font-weight:300">+123 456 789</p>
  <p class="contact__line" style="top:164px;font-size:7.5px">WWW.COMPANYNAME.COM</p>
</section>

</body>
</html>
```